We are an appraisal and dispute resolution company that works with insurance companies and insureds.

We need a website built that appeals to insurance companies as well as insureds to entrust we can assist come to a resolution with their property insurance claim.

Target Market(s)

Insurance Carriers and Insureds

Industry/Entity Type

Insurance

Coding

Coded - Design and coding required

Number of Pages Required

5+ page

Requirements
Must have
• Would like to click on pages and it take you down one page to that specific section
Nice to have
• Clean look

```html
<!DOCTYPE html>
<html lang="en">
<head>
<meta charset="utf-8">
<title>Arbiton Property Insurance</title>
<link href="https://fonts.googleapis.com/css2?family=Poppins:wght@300;400;500;600&display=swap" rel="stylesheet">
<style>
:root{
  --teal:#3ec8cb;
  --teal-dark:#2fb5b8;
  --ink:#1e1e2a;
  --text:#2a2a33;
  --muted:#6b6b74;
  --hero:#f4f4f4;
  --panel:#efefef;
  --line:#e3e3e3;
  --footer:#20202d;
  --white:#ffffff;
}
*{margin:0;padding:0;box-sizing:border-box}
html,body{width:1200px;height:4197px;overflow:hidden}
body{position:relative;font-family:'Poppins',sans-serif;color:var(--text);background:var(--white)}
.abs{position:absolute}
.h2{position:absolute;left:0;width:1200px;text-align:center;font-size:40px;line-height:50px;font-weight:400;color:var(--ink)}
.rule{position:absolute;left:580px;width:40px;height:3px;background:var(--teal)}
.small{font-size:13px;line-height:20px;color:var(--muted);font-weight:300}

/* header */
.brand{left:88px;top:16px;font-size:34px;line-height:40px;font-weight:600;letter-spacing:1px;color:var(--ink);display:flex;align-items:center;gap:10px}
.brand .dot{width:14px;height:14px;background:var(--teal)}
.brand-sub{left:90px;top:56px;font-size:7px;line-height:9px;color:var(--ink);letter-spacing:.3px}
.nav-link{position:absolute;top:32px;font-size:13px;line-height:18px;color:var(--ink);white-space:nowrap}
.login{left:1033px;top:28px;width:77px;height:26px;border:2px solid var(--teal);color:var(--teal);font-size:11px;font-weight:600;display:flex;align-items:center;justify-content:center;border-radius:2px}

/* hero */
.hero{left:0;top:0;width:1200px;height:629px;background:var(--hero)}
.hero-title{left:88px;top:248px;font-size:44px;line-height:54px;font-weight:400;color:var(--ink);white-space:nowrap}
.hero-sub{left:88px;top:304px;font-size:17px;line-height:24px;color:var(--muted);white-space:nowrap}
.hero-art{left:0;top:350px;width:745px;height:279px;background:linear-gradient(180deg,#f0f1f2 0%,#cfd4d7 55%,#3ec8cb 100%)}
.quote{left:747px;top:161px;width:363px;height:349px;background:var(--white);box-shadow:0 4px 24px rgba(0,0,0,.07)}
.quote h3{position:absolute;left:0;width:363px;text-align:center;top:50px;font-size:20px;line-height:28px;font-weight:400;color:var(--ink)}
.field{position:absolute;left:28px;width:310px;height:40px;background:#f1f1f1;font-size:12px;line-height:16px;color:var(--muted);padding:12px 16px}
.qbtn{position:absolute;left:105px;top:193px;width:155px;height:33px;background:var(--teal);color:#fff;font-size:12px;font-weight:500;display:flex;align-items:center;justify-content:center}
.qnote{position:absolute;left:0;width:363px;text-align:center;font-size:12.5px;line-height:18px;color:var(--ink)}

/* services */
.svc{position:absolute;width:300px;text-align:center}
.svc svg{display:block;margin:0 auto}
.svc h4{font-size:20px;line-height:28px;font-weight:400;color:var(--ink);margin-top:18px}
.svc p{margin-top:6px}

/* home section */
.home-title{left:88px;top:1213px;font-size:38px;line-height:46px;font-weight:400;color:var(--ink)}
.home-rule{left:88px;top:1306px;width:40px;height:3px;background:var(--teal)}
.home-text{left:90px;top:1338px;width:490px;font-size:14px;line-height:23px;color:var(--muted);font-weight:300}
.bullets{left:90px;top:1415px;list-style:none;font-size:14px;line-height:23px;color:var(--text)}
.bullets li::before{content:"";display:inline-block;width:6px;height:6px;border-radius:50%;background:var(--teal);margin-right:14px;vertical-align:middle}
.home-art{left:579px;top:1174px;width:530px;height:342px;background:radial-gradient(ellipse at 55% 60%,#dfe5e6 0%,#eef1f2 60%,#ffffff 100%);border-radius:8px}

/* cta band */
.band{left:0;top:1620px;width:1200px;height:171px;background:var(--teal)}
.band p{position:absolute;left:88px;top:58px;font-size:28px;line-height:33px;color:#fff;font-weight:400}
.band .btn{position:absolute;left:942px;top:78px;width:168px;height:36px;background:#fff;color:var(--ink);font-size:12px;font-weight:500;display:flex;align-items:center;justify-content:center}

/* benefits */
.why-bg{left:0;top:2217px;width:1200px;height:639px;background:linear-gradient(180deg,#f3f3f3,#e6e7e8)}
.card{position:absolute;top:1998px;width:300px;height:366px;background:#fff;box-shadow:0 2px 12px rgba(0,0,0,.05)}
.card .ph{height:216px}
.card h4{position:absolute;left:31px;top:240px;font-size:21px;line-height:28px;font-weight:400;color:var(--ink)}
.card p{position:absolute;left:31px;top:272px;width:240px}

.why{position:absolute;width:300px;text-align:center}
.why .tri{width:0;height:0;margin:0 auto;border-left:7px solid transparent;border-right:7px solid transparent;border-top:12px solid var(--teal)}
.why h5{font-size:16px;line-height:22px;font-weight:400;color:var(--ink);margin-top:10px}
.why p{margin-top:4px}

/* faq */
.faq{left:269px;top:3044px;width:660px}
.faq div{height:45.5px;border-bottom:1px solid var(--line);display:flex;align-items:center;justify-content:space-between;padding:0 8px;font-size:15.5px;color:var(--ink)}
.faq div:last-child{border-bottom:none}
.faq span{color:var(--teal);font-size:20px}

/* reviews */
.review{position:absolute;top:3488px;width:418px;height:223px;background:#fff;border-radius:48px;box-shadow:0 6px 28px rgba(0,0,0,.07)}
.avatar{position:absolute;left:38px;top:29px;width:72px;height:72px;border-radius:50%;background:linear-gradient(135deg,#b9b3ad,#6f6761)}
.review h6{position:absolute;left:121px;top:44px;font-size:15.5px;line-height:22px;font-weight:600;color:var(--ink);white-space:nowrap}
.stars{position:absolute;left:121px;top:66px;color:#f5b82e;font-size:17px;line-height:22px;letter-spacing:1px}
.stars i{color:#f7dfa4;font-style:normal}
.qmark{position:absolute;left:312px;top:10px;font-size:110px;line-height:110px;color:#ececec;font-family:Georgia,serif}
.review p{position:absolute;left:33px;top:118px;width:345px}

/* contact + footer */
.footer{left:0;top:3945px;width:1200px;height:252px;background:var(--footer)}
.contact{left:88px;top:3791px;width:1022px;height:212px;background-color:var(--teal);background-image:radial-gradient(rgba(255,255,255,.12) 1px,transparent 1px);background-size:6px 6px}
.contact p{position:absolute;left:65px;top:58px;font-size:38px;line-height:49px;color:#fff;font-weight:400}
.contact .btn{position:absolute;left:704px;top:93px;width:251px;height:39px;background:#fff;color:var(--ink);font-size:14px;font-weight:600;letter-spacing:.5px;display:flex;align-items:center;justify-content:center}
.fbrand{left:88px;top:4072px;font-size:44px;line-height:54px;font-weight:600;color:#fff;letter-spacing:1px}
.fbrand-sub{left:90px;top:4128px;font-size:8px;line-height:10px;color:#fff}
.flink{position:absolute;top:4087px;font-size:13.5px;line-height:18px;color:#fff;white-space:nowrap}
.copy{left:359px;top:4113px;font-size:13.5px;line-height:18px;color:#fff}
.social{position:absolute;top:4093px;width:32px;height:32px;border-radius:50%;background:#3a3a48}
.totop{left:1145px;top:4119px;width:40px;height:40px;border-radius:50%;background:var(--teal);display:flex;align-items:center;justify-content:center}
</style>
</head>
<body>

<section class="abs hero" aria-label="Hero"></section>
<div class="abs brand">ARBITON<span class="dot"></span></div>
<div class="abs brand-sub">ARBITON APPRAISAL GROUP</div>
<nav>
  <span class="nav-link" style="left:553px">Commercial Insurance</span>
  <span class="nav-link" style="left:724px">Profession</span>
  <span class="nav-link" style="left:817px">Specials</span>
  <span class="nav-link" style="left:895px">FAQ</span>
  <span class="nav-link" style="left:946px">Contact Us</span>
</nav>
<div class="abs login">LOGIN</div>

<div class="abs hero-art" role="img" aria-label="Illustration of a suburban house with trees in front of a pale city skyline"></div>
<h1 class="abs hero-title">Arbiton Property Insurance</h1>
<p class="abs hero-sub">Choose from Tenant, Landlord and Home Owner Insurance.</p>

<div class="abs quote">
  <h3>Get a Quote in 3 mins Flat!</h3>
  <div class="field" style="top:96px">Home</div>
  <div class="field" style="top:144px">Zip code</div>
  <div class="qbtn">Get Instant Quote</div>
  <div class="qnote" style="top:247px">For older or newly-built homes, call us:</div>
  <div class="qnote" style="top:274px;color:var(--teal);font-size:14px">(555) 0142-7788</div>
</div>

<h2 class="h2" style="top:748px">Property Insurance</h2>

<div class="svc" style="left:107px;top:875px">
  <svg width="76" height="76" viewBox="0 0 76 76" fill="none" stroke="#1e1e2a" stroke-width="2"><rect x="14" y="10" width="48" height="62"/><circle cx="38" cy="20" r="7" stroke="#3ec8cb"/><g fill="#1e1e2a" stroke="none"><rect x="20" y="34" width="6" height="6"/><rect x="30" y="34" width="6" height="6"/><rect x="40" y="34" width="6" height="6"/><rect x="50" y="34" width="6" height="6"/><rect x="20" y="46" width="6" height="6"/><rect x="30" y="46" width="6" height="6"/><rect x="40" y="46" width="6" height="6"/><rect x="50" y="46" width="6" height="6"/></g><rect x="32" y="58" width="12" height="14"/></svg>
  <h4>Office Insurance</h4>
  <p class="small">Lorem Ipsum is simply dummy text of the printing and typesetting industry. Lorem Ipsum has been the industry's standard .</p>
</div>
<div class="svc" style="left:450px;top:875px">
  <svg width="76" height="76" viewBox="0 0 76 76" fill="none" stroke="#1e1e2a" stroke-width="2"><circle cx="38" cy="38" r="34"/><path d="M24 30h28M26 30a12 10 0 0 1 24 0"/><circle cx="38" cy="40" r="9"/><path d="M20 68c4-10 10-14 18-14s14 4 18 14"/><path d="M36 56l2 8 2-8" stroke="#3ec8cb"/></svg>
  <h4>Construction and Engineering</h4>
  <p class="small">Lorem Ipsum is simply dummy text of the printing and typesetting industry. Lorem Ipsum has been the industry's standard .</p>
</div>
<div class="svc" style="left:790px;top:875px">
  <svg width="76" height="76" viewBox="0 0 76 76" fill="none" stroke="#1e1e2a" stroke-width="2"><path d="M6 26L38 8l32 18"/><path d="M12 24v48h52V24"/><path d="M18 30h40M18 36h40M18 42h40"/><rect x="20" y="52" width="12" height="10" stroke="#3ec8cb"/><rect x="34" y="52" width="12" height="10" stroke="#3ec8cb"/><rect x="44" y="60" width="12" height="10"/></svg>
  <h4>Factory &amp; Warehouse</h4>
  <p class="small">Lorem Ipsum is simply dummy text of the printing and typesetting industry. Lorem Ipsum has been the industry's standard .</p>
</div>

<h2 class="abs home-title">Home Insurance that’s<br>Always By Your Side</h2>
<div class="abs home-rule"></div>
<p class="abs home-text">Lorem Ipsum is simply dummy text of the printing and typesetting industry. Lorem Ipsum has been the industry's standard dummy text ever since the 1500s, when an unknown printer.</p>
<ul class="abs bullets">
  <li>Fastest Claim Settlement</li>
  <li>Unparalleled Provisions</li>
  <li>Available 24×7 though our call centre and the Mobile App</li>
</ul>
<div class="abs home-art" role="img" aria-label="Illustration of a family standing beside their house holding a heart"></div>

<section class="abs band">
  <p>Protect your home and the things you love.<br>Get Arbiton Home Direct Insurance.</p>
  <div class="btn">GET INSURED</div>
</section>

<h2 class="h2" style="top:1906px">Benefits Overview of Property Insurance</h2>
<div class="rule" style="top:1966px"></div>

<div class="abs why-bg" role="img" aria-label="Faint photo of city office towers"></div>

<div class="card" style="left:137px"><div class="ph" role="img" aria-label="Photo of a lit suburban house at dusk" style="background:linear-gradient(180deg,#7d93b8,#3a4a68 60%,#c9a36a)"></div><h4>Property Specific</h4><p class="small">Lorem Ipsum is simply dummy text of the printing and typesetting industry. Lorem Ipsum has been industry's .</p></div>
<div class="card" style="left:450px"><div class="ph" role="img" aria-label="Photo of a red fire hose reel and extinguisher on a wall" style="background:linear-gradient(90deg,#8a7f78,#b8362e 45%,#d9d6d2 80%)"></div><h4>Wide Coverage</h4><p class="small">Lorem Ipsum is simply dummy text of the printing and typesetting industry. Lorem Ipsum has been industry's .</p></div>
<div class="card" style="left:763px"><div class="ph" role="img" aria-label="Photo of a spiral notebook with project notes" style="background:linear-gradient(135deg,#e9e9ea,#c8c9cc)"></div><h4>Simple Documentation</h4><p class="small">Lorem Ipsum is simply dummy text of the printing and typesetting industry. Lorem Ipsum has been industry's .</p></div>

<h2 class="h2" style="top:2438px">Why ClaimWise</h2>

<div class="why" style="left:107px;top:2537px"><div class="tri"></div><h5>Deep Product Knowledge</h5><p class="small">Lorem Ipsum is simply dummy text of the printing and typesetting industry.</p></div>
<div class="why" style="left:450px;top:2537px"><div class="tri"></div><h5>Cost-effective Insurance</h5><p class="small">Lorem Ipsum is simply dummy text of the printing and typesetting industry.</p></div>
<div class="why" style="left:790px;top:2537px"><div class="tri"></div><h5>Quick Turnaround</h5><p class="small">Lorem Ipsum is simply dummy text of the printing and typesetting industry.</p></div>
<div class="why" style="left:107px;top:2672px"><div class="tri"></div><h5>Strong Claim Support</h5><p class="small">Lorem Ipsum is simply dummy text of the printing and typesetting industry.</p></div>
<div class="why" style="left:450px;top:2672px"><div class="tri"></div><h5>Value Added Services</h5><p class="small">Lorem Ipsum is simply dummy text of the printing and typesetting industry.</p></div>
<div class="why" style="left:790px;top:2672px"><div class="tri"></div><h5>Policy Administration</h5><p class="small">Lorem Ipsum is simply dummy text of the printing and typesetting industry.</p></div>

<h2 class="h2" style="top:2950px">FAQs</h2>
<div class="abs faq">
  <div>Who should take property insurance policy?<span>+</span></div>
  <div>What are the different kinds of policies under property insurance policies?<span>+</span></div>
  <div>Why is it important to buy property insurance?<span>+</span></div>
  <div>What are the important parameters to consider in property insurance?<span>+</span></div>
  <div>How is the premium amount determined on a property insurance policy?<span>+</span></div>
  <div>Where can I buy a property insurance policy?<span>+</span></div>
</div>

<h2 class="h2" style="top:3384px">Customer Review</h2>
<div class="rule" style="top:3446px"></div>

<div class="review" style="left:86px"><div class="avatar" role="img" aria-label="Customer portrait photo"></div><h6>Harbor Canopy</h6><div class="stars">★★★★<i>★</i></div><div class="qmark">“</div><p class="small">Lorem Ipsum is simply dummy text of the print-ing and typesetting industry. Lorem Ipsum has been the industry's standard dummy type .</p></div>
<div class="review" style="left:533px"><div class="avatar" role="img" aria-label="Customer portrait photo"></div><h6>Dana Whitfield</h6><div class="stars">★★★★<i>★</i></div><div class="qmark">“</div><p class="small">Lorem Ipsum is simply dummy text of the print-ing and typesetting industry. Lorem Ipsum has been the industry's standard dummy type .</p></div>
<div class="review" style="left:978px"><div class="avatar" role="img" aria-label="Customer portrait photo"></div><h6>Omar Reyes</h6><div class="stars">★★★★<i>★</i></div><div class="qmark">“</div><p class="small">Lorem Ipsum is simply dummy text of the print-ing and typesetting industry. Lorem Ipsum has been the industry's standard dummy type .</p></div>

<footer class="abs footer"></footer>
<section class="abs contact">
  <p>Have questions?<br>Please Contact us Today</p>
  <div class="btn">GET IN TOUCH WITH US</div>
</section>

<div class="abs fbrand">ARBITON</div>
<div class="abs fbrand-sub">ARBITON APPRAISAL GROUP</div>
<nav>
  <span class="flink" style="left:359px">Commercial Insurance</span>
  <span class="flink" style="left:543px">Profession</span>
  <span class="flink" style="left:641px">Specials</span>
  <span class="flink" style="left:725px">FAQ</span>
  <span class="flink" style="left:779px">Contact Us</span>
</nav>
<div class="abs copy">©Copyright 2021 | All Rigts Reserved</div>
<div class="social" style="left:954px"></div>
<div class="social" style="left:995px"></div>
<div class="social" style="left:1034px"></div>
<div class="social" style="left:1073px"></div>
<div class="abs totop"><svg width="12" height="8" viewBox="0 0 12 8"><path d="M1 7l5-5 5 5" stroke="#fff" stroke-width="1.6" fill="none"/></svg></div>

</body>
</html>
```